Webdesign für KFZ-Service-Betrieb
Zielgruppe
Wartung, Reparatur und Instandsetzung von Kraftfahrzeugen aller Marken.
Reifenhandel, Old- und Youngtimer-Service, An- und Verkauf von Fahrzeugen.
Aufgabenstellung
Firmenfarbe ist blau.
Moderner, Übersichtlicher und Transparenter Auftritt erwünscht.

```html
<!DOCTYPE html>
<html lang="de">
<head>
<meta charset="utf-8">
<title>Der Feldmann – Autoservice nach Maß</title>
<link href="https://fonts.googleapis.com/css2?family=Open+Sans:ital,wght@0,400;0,600;0,700;1,700&display=swap" rel="stylesheet">
<style>
:root{
  --navy:#002176;
  --blue:#0a35a3;
  --light:#7fa6f5;
  --pale:#e1e9fb;
  --ink:#111;
  --night:#030a24;
  --white:#fff;
}
*{box-sizing:border-box;margin:0;padding:0}
html,body{width:1200px;height:2247px;overflow:hidden}
body{position:relative;font-family:"Open Sans",Arial,sans-serif;color:var(--ink);background:var(--white)}
.abs{position:absolute}
/* hero */
.hero{left:0;top:0;width:1200px;height:344px;background:linear-gradient(100deg,#3a3a40 0%,#6b6c72 40%,#9a9ca3 60%,#4a4b50 100%)}
.hours{left:60px;top:68px;width:526px;height:32px;background:var(--navy);color:var(--white);font-size:13.5px;font-weight:700;line-height:32px;padding-left:24px}
.hours em{font-style:normal;color:var(--light)}
.brand{left:60px;top:102px;width:526px;height:139px;background:var(--white);display:flex;align-items:center;padding-left:28px;gap:22px}
.brand-mark{width:26px;height:26px;border-radius:50%;background:var(--blue);flex:none}
.brand-name{font-size:40px;font-weight:600;color:var(--blue);line-height:1.05}
.brand-tag{font-size:24px;font-weight:600;color:var(--blue);margin-top:4px}
.claim{left:60px;top:244px;width:268px;height:31px;background:var(--light);color:var(--navy);font-weight:700;font-size:15px;line-height:31px;padding-left:24px}
/* nav */
.nav{left:0;top:344px;width:1200px;height:70px;background:var(--navy);display:flex;align-items:center;padding-left:40px}
.nav a{color:var(--white);text-decoration:none;font-weight:700;font-size:16px;padding:0 26px;border-right:1px solid #6c84c8;line-height:36px}
.nav a:last-child{border-right:0}
.nav a.current{color:var(--light)}
/* tyres */
.tyres{left:0;top:414px;width:1200px;height:318px;background:linear-gradient(#fff 0%,#e5ecfb 40%,#aac3f0 100%)}
.tyres-img{left:74px;top:56px;width:416px;height:176px;border-radius:50%/40%;background:radial-gradient(#6b6f78,#2a2c31 60%,rgba(40,40,45,0) 72%)}
.tyres-text{left:523px;top:38px;width:640px;font-size:14.5px;line-height:18px}
.tyres-text h2{font-size:23px;font-weight:600;margin-bottom:16px}
.btn{display:inline-block;background:var(--blue);color:var(--white);font-weight:700;font-size:15px;text-decoration:none}
.tyres-text .btn{padding:0 18px;line-height:37px;margin:10px 0 20px}
.sign{font-style:italic;font-weight:700;margin-top:18px}
.sign span{display:block;color:var(--blue)}
/* offers */
.offers{left:0;top:732px;width:1200px;height:325px;background:linear-gradient(#2b5fb8 0%,#7ea6db 30%,#c9d6e4 45%,#3d7a28 60%,#8c8c8c 80%,#7a7a7a 100%)}
.offers h2{position:absolute;top:40px;width:100%;text-align:center;color:var(--white);font-size:24px;font-weight:600}
.card{position:absolute;top:108px;width:153px;box-shadow:0 2px 4px rgba(0,0,0,.3)}
.card-head{height:46px;background:var(--light);color:var(--navy);font-weight:600;font-size:15px;line-height:17px;padding:4px 7px;display:flex;align-items:flex-end}
.card-body{background:var(--pale);color:var(--blue);font-size:13.5px;line-height:16.5px;padding:8px 7px;height:90px}
.card-price{background:var(--white);color:var(--navy);font-weight:700;font-size:15px;height:37px;line-height:37px;padding-left:7px}
/* intro */
.intro{left:253px;top:1098px;width:700px;font-size:14.5px;line-height:18px}
.intro h2{font-size:23px;font-weight:600;margin-bottom:14px}
.intro p{margin-bottom:18px}
.cta{left:504px;top:1290px;width:193px;height:38px;line-height:38px;text-align:center}
/* teaser */
.teaser{left:0;top:1374px;width:1200px;height:341px;background:var(--navy)}
.teaser-card{position:absolute;top:47px;width:181px;height:254px;box-shadow:0 3px 5px rgba(0,0,0,.4)}
.teaser-pic{height:180px;background:var(--white);display:flex;align-items:center;justify-content:center}
.teaser-pic div{width:152px;height:152px;border-radius:50%}
.teaser-label{height:74px;background:var(--light);color:var(--navy);font-weight:600;font-size:14.5px;line-height:16.5px;text-align:center;display:flex;align-items:center;justify-content:center;padding:0 20px}
/* contact */
.contact{left:0;top:1715px;width:1200px;height:532px;background:var(--night);color:var(--white)}
.contact h2{position:absolute;left:165px;top:38px;font-size:23px;font-weight:600}
.address{position:absolute;left:165px;top:103px;font-size:15px;line-height:27.7px}
.address .hl{color:var(--light)}
.address .gap{height:27.7px}
.form label{position:absolute;right:523px;color:var(--light);font-size:15px}
.form .field{position:absolute;left:705px;width:331px;height:28px;background:var(--white)}
.send{position:absolute;left:925px;top:402px;width:111px;height:37px;line-height:37px;text-align:center}
</style>
</head>
<body>

<header>
  <div class="abs hero" role="img" aria-label="Foto: Mechaniker mit Handschuhen arbeitet im Motorraum eines Autos"></div>
  <div class="abs hours"><em>Montag - Freitag</em> 07.30 Uhr - 18.00 Uhr <em>Samstag</em> 09.00 Uhr - 12.00 Uhr</div>
  <div class="abs brand">
    <span class="brand-mark"></span>
    <div>
      <div class="brand-name">Der Feldmann</div>
      <div class="brand-tag">Autoservice nach Maß</div>
    </div>
  </div>
  <div class="abs claim">Alle Marken - Alle Leistungen</div>
  <nav class="abs nav">
    <a class="current" href="#">START</a>
    <a href="#">LEISTUNGEN</a>
    <a href="#">PHILOSOPHIE</a>
    <a href="#">FIRMENGESCHICHTE</a>
    <a href="#">ZUFRIEDENE KUNDEN</a>
    <a href="#">TEAM UND KONTAKT</a>
  </nav>
</header>

<section class="abs tyres">
  <div class="abs tyres-img" role="img" aria-label="Foto: Reihe von Sommerreifen mit Alufelgen"></div>
  <div class="abs tyres-text">
    <h2>Jetzt günstige Sommerreifen/Sommerräder kaufen!</h2>
    <p>Bei uns gibt es Markenreifen schon ab 39,- Euro<br>wir liefern alle Fabrikate zu günstigen Preisen.</p>
    <a class="btn" href="#">Fragen Sie nach Ihrem individuellen Angebot</a>
    <p>Montage-Preis ab 9,50 Euro (pro Rad)<br>Räderwechsel-Preise 12,90 / 14,90 / 19,90 pro Fahrzeug.</p>
    <p class="sign">Wir freuen uns auf Ihre Anfrage.<span>Der Feldmann - Autoservice nach Maß</span></p>
  </div>
</section>

<section class="abs offers" role="img" aria-label="Hintergrundfoto: Landstraße durch grüne Felder unter blauem Himmel">
  <h2>Aktuelle Angebote</h2>
  <div class="card" style="left:74px"><div class="card-head">10-Punkte Frühjahrs-Check</div><div class="card-price">nur 19,90 €</div></div>
  <div class="card" style="left:253px"><div class="card-head">Rädereinlagerung</div><div class="card-price">nur 19,90 €</div></div>
  <div class="card" style="left:433px"><div class="card-head">Räderwäsche</div><div class="card-price">nur 16,00 €</div></div>
  <div class="card" style="left:612px"><div class="card-head">Komplett-<br>versiegelung</div><div class="card-body">des Unterbodens mit PROTEKTA zum kalkulierten Festpreis</div><div class="card-price">ab 249,00 €</div></div>
  <div class="card" style="left:792px"><div class="card-head">Fahrzeugkomplett-<br>aufbereitung</div><div class="card-body">inkl. Lackreinigung, Politur &amp; Lackver-siegelung, Innen-reinigung</div><div class="card-price">ab 149,00 €</div></div>
  <div class="card" style="left:973px"><div class="card-head">Markenreifen</div><div class="card-price">ab 39,00 €</div></div>
</section>

<section>
  <div class="abs intro">
    <h2>Lorem ipsum</h2>
    <p>Lorem ipsum dolor sit amet, consectetuer adipiscing elit. Aenean commodo ligula eget dolor. Aenean massa. Cum sociis natoque penatibus et magnis dis parturient montes, nascetur ridiculus mus. Donec quam felis, ultricies nec, pellentesque eu, pretium quis, sem. Nulla consequat massa.</p>
    <p>quis enim. Donec pede justo, fringilla vel, aliquet nec, vulputate eget, arcu. In enim justo, rhoncus ut, imperdiet a, venenatis vitae, justo. Nullam dictum felis eu pede mollis</p>
  </div>
  <a class="abs btn cta" href="#">Kontaktieren Sie uns!</a>
</section>

<section class="abs teaser">
  <div class="teaser-card" style="left:239px">
    <div class="teaser-pic"><div role="img" aria-label="Foto: Mechaniker arbeitet unter einem Fahrzeug" style="background:radial-gradient(#8a7a6a,#3c3530)"></div></div>
    <div class="teaser-label">Hier erfahren Sie mehr über unsere Leistungen</div>
  </div>
  <div class="teaser-card" style="left:510px">
    <div class="teaser-pic"><div role="img" aria-label="Foto: Mechaniker montiert ein Rad an einem roten Auto" style="background:radial-gradient(#b04040,#2a2d3a)"></div></div>
    <div class="teaser-label">Wollen Sie mehr über unsere Philosophie erfahren?</div>
  </div>
  <div class="teaser-card" style="left:779px">
    <div class="teaser-pic"><div role="img" aria-label="Historisches Foto: Werkstatt mit Kutsche" style="background:radial-gradient(#a39b88,#4d473d)"></div></div>
    <div class="teaser-label">Unsere Firmen-geschichte begann vor sechs Generationen...</div>
  </div>
</section>

<footer class="abs contact">
  <h2>Nehmen Sie Kontakt zu uns auf</h2>
  <div class="address">
    Der Feldmann GmbH<br>Lindenweg 14<br>95000 Musterstadt
    <div class="gap"></div>
    <span class="hl">Telefon: 01234 / 56 70<br>Telefax: 01234 / 56 72 22</span>
    <div class="gap"></div>
    <span class="hl">E-Mail: info@derfeldmann-auto.example<br>Web: www.derfeldmann-auto.example</span>
    <div class="gap"></div>
    <span class="hl">Geschäftsführer:<br>Jonas K. Brehmer</span>
  </div>
  <form class="form">
    <label style="top:111px">Name</label><div class="field" style="top:107px"></div>
    <label style="top:157px">E-Mail</label><div class="field" style="top:153px"></div>
    <label style="top:203px">Betreff</label><div class="field" style="top:199px"></div>
    <label style="top:249px">Nachricht</label><div class="field" style="top:245px;height:139px"></div>
    <a class="btn send" href="#">Absenden</a>
  </form>
</footer>

</body>
</html>
```